Wine label design for my wife. Wine called "The Mirabel"

I need a wine label face lift of one of my premium wines in my collection. My wine sells in Harbor Lark's all over the States. My current label is called The Mirabel (my wife's name) and the illustration of her eyes is done by a well know artist from South Africa. I do not have to use this illustration and therefor I attached several pictures of her and her eyes, even when she was a little girl. The wine's also made in South Africa. This is a premium wine that we only sell 2000 bottles per year. The wine sells at 60 usd per bottle, The current label is too white. I also think her eyes should look more at the person buying it, than away from them.

Target Market(s)

Top end wine buyers

Font styles to use
Decorative
Script

Requirements
Must have
• 'The Mirabel' must be on the label
An illustration must be on the label
Basically all the info that's on the current label must be on by law. As per Sample
Nice to have
• Maybe some ideas of her whole face?
Should not have
• any gold colour

```html
<!DOCTYPE html>
<html lang="en">
<head>
<meta charset="utf-8">
<title>The Mirabel – Sauvignon Blanc Label</title>
<link href="https://fonts.googleapis.com/css2?family=Cormorant+SC:wght@400&family=Italianno&display=swap" rel="stylesheet">
<style>
  :root {
    --backdrop: #f1f0eb;
    --label-black: #1c1c1d;
    --label-sheen: #2a2a2c;
    --ink-light: #e4e2dc;
    --eye-teal: #19c4bd;
    --eye-teal-deep: #0e8f8d;
    --copper: #c9561c;
  }
  * { box-sizing: border-box; margin: 0; padding: 0; }
  html, body {
    width: 1200px;
    height: 1200px;
    overflow: hidden;
    background: var(--backdrop);
  }
  .canvas {
    position: relative;
    width: 1200px;
    height: 1200px;
  }
  .label {
    position: absolute;
    left: 280px;
    top: 97px;
    width: 640px;
    height: 1006px;
    background: radial-gradient(ellipse at 55% 35%, var(--label-sheen) 0%, var(--label-black) 70%);
    color: var(--ink-light);
    text-align: center;
  }
  .label__brand {
    position: absolute;
    top: 78px;
    left: 0;
    right: 0;
    font-family: "Cormorant SC", serif;
    font-size: 34px;
    font-weight: 400;
    letter-spacing: 0.1em;
    line-height: 1.2;
    color: var(--ink-light);
  }
  .label__portrait {
    position: absolute;
    left: 80px;
    top: 300px;
    width: 475px;
    height: 175px;
    background:
      radial-gradient(ellipse 75px 65px at 80px 95px, var(--eye-teal) 0%, var(--eye-teal-deep) 50%, transparent 78%),
      radial-gradient(ellipse 115px 75px at 370px 90px, var(--eye-teal) 0%, var(--eye-teal-deep) 50%, transparent 78%);
    opacity: 0.85;
  }
  .label__name {
    position: absolute;
    top: 595px;
    left: 0;
    right: 0;
    font-family: "Italianno", cursive;
    font-size: 112px;
    font-weight: 400;
    line-height: 1.1;
    color: var(--copper);
  }
  .label__varietal {
    position: absolute;
    top: 826px;
    left: 0;
    right: 0;
    font-family: "Cormorant SC", serif;
    font-size: 34px;
    letter-spacing: 0.1em;
    line-height: 1.2;
  }
  .label__vintage {
    position: absolute;
    top: 868px;
    left: 0;
    right: 0;
    font-family: "Cormorant SC", serif;
    font-size: 34px;
    letter-spacing: 0.08em;
    line-height: 1.2;
  }
</style>
</head>
<body>
  <main class="canvas">
    <section class="label">
      <p class="label__brand">Daniel Thorne Wines</p>
      <div class="label__portrait" role="img" aria-label="Teal foil illustration of a woman's eyes and eyebrows looking at the viewer"></div>
      <h1 class="label__name">The Mirabel</h1>
      <p class="label__varietal">Sauvignon Blanc</p>
      <p class="label__vintage">2017</p>
    </section>
  </main>
</body>
</html>
```